Flyer-Design für Metall- und Blechverarbeitung
Zielgruppe
Metall- und Blechverarbeitung
https://kantwerk-nord.de/
https://kantwerk-nord.de/leistungen/sonderanfertigungen/
Aufgabenstellung
-modernes Design
-DIN A5 - 2 Seitig
-bei diesem Flyer wird nur ein Dekoprodukt angesprochen, welches in verschiedenen Größen erhältlich ist, grundsätzlich gibt es aber Standartmaße. Nach Wunsch auch verzinkt und in Farbe erhältlich
-ich hab viele Bilder verfügbar, konnte nicht alles hochladen - kann es per .zip zusenden
Preise / Maße:
646 x 627 mm, Material: S235 roh > 80 EUR
962 x 940 mm, Material: S235 roh > 120 EUR
804 x 784 mm, Material: S235 roh > 90 EUR
204 x 205 mm, Material: S235, weiß beschichtet (nur für Innen) > 20 EUR
- auf Wunsch auch in verschiedenen Farben pulverbeschichtet gegen Aufpreis erhältlich

```html
<!DOCTYPE html>
<html lang="de">
<head>
<meta charset="utf-8">
<title>Deko-Herzen aus Metall – Flyer</title>
<link rel="stylesheet" href="https://fonts.googleapis.com/css2?family=Josefin+Sans:wght@400;600&family=Open+Sans:wght@400;600;700&display=swap">
<style>
  :root{
    --bg:#dfe5ec;
    --paper:#f7f7f6;
    --green:#2f7d32;
    --green-dark:#2a6e2c;
    --head-grey:#6d727a;
    --row-grey:#a7b1bb;
    --text:#2a2a2a;
    --muted:#8a8f95;
    --white:#ffffff;
  }
  *{box-sizing:border-box;margin:0;padding:0}
  html,body{width:1200px;height:1200px;overflow:hidden}
  body{background:var(--bg);font-family:"Open Sans",sans-serif;color:var(--text);position:relative}
  .flyer{position:absolute;left:220px;top:62px;width:760px;height:1075px;background:var(--paper);
    box-shadow:0 18px 40px rgba(40,60,80,.18);display:flex;flex-direction:column}
  .brand{height:185px;display:flex;flex-direction:column;align-items:center;justify-content:center;gap:12px}
  .brand-name{display:flex;align-items:center;gap:12px;font-family:"Open Sans",sans-serif;font-weight:700;
    font-size:44px;color:var(--green);letter-spacing:-.5px}
  .brand-dot{width:16px;height:16px;border-radius:50%;background:var(--green)}
  .brand-tagline{font-size:12px;letter-spacing:4px;color:var(--muted);text-transform:uppercase}
  .hero{height:455px;background:linear-gradient(180deg,#e9ecee 0%,#c9ccce 35%,#6a5e50 60%,#b8b2a8 82%,#d8dadc 100%)}
  .headline{font-family:"Josefin Sans",sans-serif;font-weight:600;font-size:60px;color:var(--green);
    text-transform:uppercase;padding:26px 40px 12px;letter-spacing:-.5px;line-height:1}
  .prices{margin:0 40px;width:calc(100% - 80px);border-collapse:collapse;font-size:19px}
  .prices th{background:var(--head-grey);color:var(--white);font-weight:700;text-align:left;padding:5px 16px}
  .prices td{padding:4px 16px}
  .prices tr:nth-child(even) td{background:var(--row-grey)}
  .prices .price{text-align:right}
  .note{margin:14px 40px 0;font-size:14.5px;color:var(--text)}
  .footer{margin-top:auto;height:165px;background:var(--green);color:var(--white);
    display:flex;flex-direction:column;align-items:center;justify-content:center;gap:10px}
  .footer-company{font-weight:700;font-size:17px}
  .footer-contact{display:flex;font-size:15.5px;line-height:1.4}
  .footer-address{text-align:right;padding-right:14px;border-right:1px solid var(--white)}
  .footer-reach{padding-left:14px}
</style>
</head>
<body>
  <article class="flyer">
    <header class="brand">
      <div class="brand-name"><span>Kantwerk Nord</span><span class="brand-dot"></span></div>
      <div class="brand-tagline">Laserschneid &amp; Abkanttechnik</div>
    </header>
    <div class="hero" role="img" aria-label="Foto: drei Deko-Herzen aus Metall, gefüllt mit Holzscheiten, vor einer hellen Wand im Schnee"></div>
    <h1 class="headline">Deko-Herzen aus Metall</h1>
    <table class="prices">
      <thead><tr><th>Maße</th><th>Material *</th><th class="price">Preis</th></tr></thead>
      <tbody>
        <tr><td>646 x 627 mm</td><td>S235 roh</td><td class="price">80,00 €</td></tr>
        <tr><td>962 x 940 mm</td><td>S235 roh</td><td class="price">120,00 €</td></tr>
        <tr><td>804 x 784 mm</td><td>S235 roh</td><td class="price">90,00 €</td></tr>
        <tr><td>204 x 205 mm</td><td>S235 weiß (Innenraum)</td><td class="price">20,00 €</td></tr>
      </tbody>
    </table>
    <p class="note">* Auf Wunsch auch in verschiedenen Farben pulverbeschichtet gegen Aufpreis erhältlich</p>
    <footer class="footer">
      <div class="footer-company">Laserschneid &amp; Abkanttechnik Jonas Brandtner e.K.</div>
      <div class="footer-contact">
        <div class="footer-address">Lindenhofer Str. 14<br>99974 Lindenhof<br>Thüringen, Deutschland</div>
        <div class="footer-reach">+49 (0)36021.5540-00<br>info@kantwerk-nord.de<br>www.kantwerk-nord.de</div>
      </div>
    </footer>
  </article>
</body>
</html>
```